Corporate brochure design 4 pages

Hi,

We are a real estate company based in Europe.

We have almost finalized a rebranding.

We are developing a brand book guidelines (still on working process) to help you undertstand the look and feel of our new CI. I would like to receive proposals of design for a corporate brochure template. I need to receive the Indesign files with full ownership rights to be able to adapt all our documentation with this template.
Regarding the images, you can take gabaris on www.pelvaromedia.com. I will be able to take them afterwards.

There will be 4 pages. you will receive the 4 pages on pdf for your consideration with our (almost) actual layout.

- 1st page: cover
- 2nd page: company presentation in french and english
- 3rd page: some market data + graph
- 4th page: 2 retail centers presentation.

In the template, i need to have:
- the paragraph styles in order
- 2 different masters with top/bottom/page number aso.

Please feel free to ask any other questions.

best regards,
Updates

I would like to precise tha t we are active on the commercial real estate sector:

- office transactions (rent /sales)
- property management of administrative and business buildings
- Valuation of properties
- Capital markets (investment advices for selling building)

Industry/Entity Type

Real Estate

Colors

Designer to choose colors to be used in the design.

```html
<!DOCTYPE html>
<html lang="fr">
<head>
<meta charset="utf-8">
<title>Meridane – Brochure</title>
<link href="https://fonts.googleapis.com/css2?family=Roboto:wght@300;400;700;900&display=swap" rel="stylesheet">
<style>
:root{
  --orange:#f0641e;
  --ink:#3c3c3c;
  --dark:#1f1f1f;
  --grey:#9e9e9e;
  --band:#ececec;
  --bar:#a3a3a3;
  --paper:#ffffff;
}
*{margin:0;padding:0;box-sizing:border-box}
html,body{width:1200px;height:849px;overflow:hidden;background:var(--paper)}
body{font-family:"Roboto",Arial,sans-serif;font-weight:300;color:var(--ink);position:relative}
.page{position:absolute;top:0;width:600px;height:849px}
.page--left{left:0}
.page--right{left:600px}
.running-head{position:absolute;top:44px;left:43px;display:flex;gap:8px}
.running-head .slash{width:14px;height:36px}
.running-head p{font-size:12.4px;line-height:15px;text-transform:uppercase;color:var(--ink);padding-top:3px}
.brand{position:absolute;top:44px;right:46px;font-weight:900;font-size:27px;letter-spacing:-1px;color:var(--dark)}
.photo{position:absolute;left:43px;top:123px;width:514px;height:353px;background:linear-gradient(135deg,#d9d9d9,#8c8c8c 55%,#5a5a5a)}
.caption{position:absolute;left:43px;top:482px;font-size:10.5px;color:var(--ink)}
.col{position:absolute;width:243px}
.col h2{font-size:12.5px;font-weight:400;color:var(--orange);margin-bottom:14px;text-transform:uppercase}
.col p{font-size:9.4px;line-height:12.3px;text-align:justify;margin-bottom:12px}
.folio{position:absolute;top:805px;font-size:10px;color:var(--grey)}
.data-table{position:absolute;left:0;top:0;width:600px}
.thead{position:absolute;top:227px;font-size:9.8px;text-transform:uppercase}
.row{position:absolute;left:221px;width:336px;height:14px;font-size:9.4px;line-height:14px}
.row.band{background:var(--band)}
.row span{position:absolute}
.row .name{left:4px}
.row .m2{right:103px}
.row .pct{right:3px}
.row.total{color:var(--orange)}
.zone{position:absolute;left:48px;font-size:9.4px;text-transform:uppercase}
.zone b{font-weight:300;color:var(--orange)}
.chart{position:absolute;left:0;top:0}
.source{position:absolute;left:42px;top:771px;font-size:9px}
</style>
</head>
<body>

<section class="page page--left">
  <div class="running-head">
    <svg class="slash" viewBox="0 0 14 36"><line x1="12" y1="1" x2="2" y2="35" stroke="#f0641e" stroke-width="2.2"/></svg>
    <p>A propos de nous<br>About us</p>
  </div>
  <div class="brand">MERIDANE</div>
  <div class="photo" role="img" aria-label="Portrait photo of the four partners of the team in an office setting"></div>
  <p class="caption">Luc Damarin, Paul Heyvaert, Joris Lemmel, Erik Vandorn</p>

  <article class="col" style="left:43px;top:536px">
    <h2>Une équipe</h2>
    <p>Proposer des services de qualité répondant parfaitement à vos attentes est notre ambition. Elle est partagée par tous les membres de notre équipe.</p>
    <p>Notre connaissance du marché luxembourgeois, nos compétences et notre engagement dans les missions qui nous sont confiées font de Meridane l’acteur majeur de l’immobilier d’entreprise au Grand-Duché. Nous sommes fiers de cette position et nous travaillons tous les jours pour la conserver.</p>
    <p>Viser l’excellence suppose de savoir améliorer sans cesse nos prestations pour répondre le plus précisément à vos besoins. Venez nous consulter, vous constaterez que nos collaborateurs prennent le temps de vous écouter pour bien comprendre votre demande. Leur professionnalisme, leur savoir-faire et leur mobilisation nous permettront de trouver la solution.</p>
  </article>
  <article class="col" style="left:314px;top:536px">
    <h2>A team</h2>
    <p>Our ambition is to offer quality services that perfectly meet your expectations. This ambition is shared by all members of the team.</p>
    <p>Thanks to our knowledge of the Luxembourg market, our skills and our commitment to the missions entrusted to us, Meridane is the undisputed leader in commercial real estate in the Grand Duchy. We are proud of this position and work hard to deserve it every day.</p>
    <p>Targeting excellence means the constant improvement of our services in order to more accurately meet your needs. When you meet with us, you will find that our employees take the necessary time to listen to you and to correctly understand your need. Their professionalism, know-how and mobilisation will ensure that we find the right solution.</p>
  </article>
  <span class="folio" style="left:43px">/ 2</span>
</section>

<section class="page page--right">
  <div class="running-head">
    <svg class="slash" viewBox="0 0 14 36"><line x1="12" y1="1" x2="2" y2="35" stroke="#f0641e" stroke-width="2.2"/></svg>
    <p>Rapport de marché bureaux Luxembourg Q3-2013<br>Luxembourg office market report Q3-2013</p>
  </div>
  <div class="brand">MERIDANE</div>

  <article class="col" style="left:42px;top:124px">
    <h2>Stock</h2>
    <p>Le stock de mètres carrés disponibles de bureaux a augmenté de 0,36 % au troisième trimestre de cette année grâce à la livraison de près de 12 300 m². Le stock total équivaut à 3 465 600 m².</p>
  </article>
  <article class="col" style="left:314px;top:124px">
    <h2>Stock</h2>
    <p>The stock of available office square meters has increased by 0.36% during the third quarter of this year with the delivery of 12,300 m2. The total stock reaches 3,465,600 sm2.</p>
  </article>

  <div class="data-table">
    <span class="thead" style="left:226px">Quartiers-districts</span>
    <span class="thead" style="left:401px">Stock m2</span>
    <span class="thead" style="left:506px">Stock %</span>

    <span class="zone" style="top:245px">Centre-ville <b>/</b> City</span>
    <span class="zone" style="top:386px">Ville-périphérie <b>/</b> City-periphery</span>
    <span class="zone" style="top:464px">Périphérie <b>/</b> Periphery</span>

    <div class="row band" style="top:244px"><span class="name">Kirchberg</span><span class="m2">915 000</span><span class="pct">26,42 %</span></div>
    <div class="row band" style="top:260px"><span class="name">CBD</span><span class="m2">806 400</span><span class="pct">23,27 %</span></div>
    <div class="row band" style="top:275px"><span class="name">Station</span><span class="m2">382 700</span><span class="pct">11,04 %</span></div>
    <div class="row band" style="top:291px"><span class="name">Cloche d’Or</span><span class="m2">365 600</span><span class="pct">10,55 %</span></div>
    <div class="row band" style="top:307px"><span class="name">Limpertsberg</span><span class="m2">85 000</span><span class="pct">2,45 %</span></div>
    <div class="row band" style="top:322px"><span class="name">Belair / Merl</span><span class="m2">67 800</span><span class="pct">1,96 %</span></div>
    <div class="row band" style="top:338px"><span class="name">Hamm</span><span class="m2">44 500</span><span class="pct">1,28 %</span></div>
    <div class="row band" style="top:354px"><span class="name">Kalchesbrück</span><span class="m2">33 000</span><span class="pct">0,95 %</span></div>
    <div class="row total" style="top:369px"><span class="name">TOTAL</span><span class="m2">2 700 500</span><span class="pct">77,92 %</span></div>
    <div class="row band" style="top:385px"><span class="name">Airport - Findel</span><span class="m2">157 500</span><span class="pct">4,54 %</span></div>
    <div class="row band" style="top:401px"><span class="name">Bertrange / Bourmicht</span><span class="m2">82 000</span><span class="pct">2,37 %</span></div>
    <div class="row band" style="top:416px"><span class="name">Strassen</span><span class="m2">81 050</span><span class="pct">2,34 %</span></div>
    <div class="row band" style="top:432px"><span class="name">Howald</span><span class="m2">62 600</span><span class="pct">1,81 %</span></div>
    <div class="row total" style="top:448px"><span class="name">TOTAL</span><span class="m2">383 150</span><span class="pct">11,06 %</span></div>
    <div class="row band" style="top:463px"><span class="name">Belval</span><span class="m2">93 090</span><span class="pct">2,69 %</span></div>
    <div class="row band" style="top:479px"><span class="name">Capellen</span><span class="m2">69 500</span><span class="pct">2,01 %</span></div>
    <div class="row band" style="top:495px"><span class="name">Leudelange</span><span class="m2">73 556</span><span class="pct">2,12 %</span></div>
    <div class="row band" style="top:510px"><span class="name">Munsbach</span><span class="m2">60 100</span><span class="pct">1,73 %</span></div>
    <div class="row band" style="top:526px"><span class="name">Windhof</span><span class="m2">40 600</span><span class="pct">1,17 %</span></div>
    <div class="row band" style="top:542px"><span class="name">Esch-sur-Alzette</span><span class="m2">24 700</span><span class="pct">0,71 %</span></div>
    <div class="row band" style="top:557px"><span class="name">Contern</span><span class="m2">20 400</span><span class="pct">0,59 %</span></div>
    <div class="row total" style="top:573px"><span class="name">TOTAL</span><span class="m2">381 946</span><span class="pct">11,02 %</span></div>
    <div class="row total" style="top:589px"><span class="name">TOTAL</span><span class="m2">3 465 596</span></div>
  </div>

  <svg class="chart" width="600" height="849" viewBox="0 0 600 849" font-family="Roboto, Arial, sans-serif" font-weight="300">
    <g font-size="7.5" fill="#3c3c3c" text-anchor="end">
      <text x="256" y="638">m²</text>
      <text x="244" y="657">3.500</text>
      <text x="244" y="679">3.000</text>
      <text x="244" y="700">2.500</text>
      <text x="244" y="722">2.000</text>
      <text x="244" y="743">1.500</text>
      <text x="244" y="765">1.000</text>
    </g>
    <g stroke="#9e9e9e" stroke-width="0.8">
      <line x1="250" y1="654" x2="250" y2="763"/>
      <line x1="250" y1="763" x2="561" y2="763"/>
      <line x1="248" y1="676" x2="252" y2="676"/>
      <line x1="248" y1="698" x2="252" y2="698"/>
      <line x1="248" y1="719" x2="252" y2="719"/>
      <line x1="248" y1="741" x2="252" y2="741"/>
    </g>
    <g fill="#a3a3a3">
      <rect x="273" y="710" width="21" height="52"/>
      <rect x="299" y="701" width="21" height="61"/>
      <rect x="326" y="697" width="21" height="65"/>
      <rect x="352" y="693" width="21" height="69"/>
      <rect x="379" y="686" width="21" height="76"/>
      <rect x="405" y="679" width="21" height="83"/>
      <rect x="431" y="668" width="21" height="94"/>
      <rect x="458" y="666" width="21" height="96"/>
      <rect x="484" y="662" width="21" height="100"/>
      <rect x="511" y="658" width="21" height="104"/>
      <rect x="537" y="656" width="21" height="106"/>
    </g>
    <g font-size="7" fill="#f0641e" text-anchor="middle">
      <text x="283" y="705">2,211</text>
      <text x="310" y="696">2,409</text>
      <text x="336" y="692">2,502</text>
      <text x="363" y="688">2,600</text>
      <text x="389" y="681">2,770</text>
      <text x="415" y="674">2,912</text>
      <text x="442" y="663">3,170</text>
      <text x="468" y="661">3,225</text>
      <text x="495" y="657">3,325</text>
      <text x="521" y="653">3,406</text>
      <text x="547" y="650">3,465</text>
    </g>
    <g font-size="7.5" fill="#3c3c3c" text-anchor="middle">
      <text x="283" y="779">2003</text>
      <text x="310" y="779">2004</text>
      <text x="336" y="779">2005</text>
      <text x="363" y="779">2006</text>
      <text x="389" y="779">2007</text>
      <text x="415" y="779">2008</text>
      <text x="442" y="779">2009</text>
      <text x="468" y="779">2010</text>
      <text x="495" y="779">2011</text>
      <text x="521" y="779">2012</text>
      <text x="547" y="779">YTD</text>
      <text x="548" y="788">2013</text>
    </g>
  </svg>
  <p class="source">Source: Axial Office Research</p>
  <span class="folio" style="right:43px">/ 3</span>
</section>

</body>
</html>
```